Dariel’s letterhead for local government

I require a letterhead for quarterly communications with constituents. The colours I have used in the past are navy & green (together) so I’m happy to use similar colours for this. Please refer to business card as an example.
The letter must make reference to the position I hold which is as per below
“Clr Dariel Kostovenko OAM”
And the tag line I have used in the past is “Dariel in Darwin”. Although I’m not sure if this would be used in a letterhead or not. Happy for this to be provided as an option.
I would like a photo in the letterhead as I believe face recognition is key as an elected member.

Target Market(s)

Political interests

Industry/Entity Type

Government Office

Font styles to use
Sans Serif

Requirements
Must have
• Politically professional. I have been an elected member for 2 years so it is expected that the letterhead conveys that. The colours of the business card is to be used.
Nice to have
• Background of photos to be manipulated or changed to make me stand out, if possible?
Should not have
• Looked like it’s cropped or undertaken by an amateur designer.

```html
<!DOCTYPE html>
<html lang="en">
<head>
<meta charset="utf-8">
<title>Dariel Kostovenko – Letterhead</title>
<link rel="stylesheet" href="https://fonts.googleapis.com/css2?family=Arimo:wght@400;700&family=Open+Sans:wght@400;600&display=swap">
<style>
  :root {
    --navy: #1e4f8a;
    --footer-navy: #2a5f93;
    --green: #22a84a;
    --green-bar: #3db35a;
    --ink: #444444;
    --ink-dark: #333333;
    --paper: #ffffff;
    --backdrop: #e9eaec;
    --photo-light: #dcdde0;
    --photo-dark: #b9bcc2;
  }
  * { margin: 0; padding: 0; box-sizing: border-box; }
  html, body { width: 1040px; height: 1200px; overflow: hidden; }
  body {
    background: var(--backdrop);
    font-family: "Open Sans", Arial, sans-serif;
    color: var(--ink);
    position: relative;
  }
  .letterhead {
    position: absolute;
    left: 66px; top: 15px;
    width: 908px; height: 1170px;
    background: var(--paper);
    box-shadow: 0 2px 10px rgba(0,0,0,0.15);
  }
  .top-bar {
    position: absolute; left: 0; top: 0; width: 100%; height: 10px;
    background: var(--green-bar);
  }
  .portrait {
    position: absolute; left: 87px; top: 36px;
    width: 186px; height: 186px; border-radius: 5px;
    background: linear-gradient(160deg, var(--photo-light) 0%, var(--photo-light) 45%, var(--photo-dark) 100%);
  }
  .identity { position: absolute; left: 304px; top: 95px; font-family: "Arimo", Arial, sans-serif; }
  .identity__name { font-size: 25px; font-weight: 700; color: var(--navy); line-height: 30px; }
  .identity__role { margin-top: 11px; font-size: 20px; color: var(--green); line-height: 25px; }
  .meta, .recipient, .salutation, .letter-body, .sign-off, .signatory {
    position: absolute; left: 85px; font-size: 14.5px;
  }
  .meta { top: 249px; }
  .recipient { top: 283px; line-height: 18px; }
  .salutation { top: 385px; }
  .letter-body { top: 430px; width: 734px; }
  .letter-body p {
    line-height: 26.4px; text-align: justify; hyphens: auto;
    margin-bottom: 26.4px;
  }
  .sign-off { top: 831px; }
  .signatory { top: 906px; }
  .signatory__name { font-size: 17px; font-weight: 600; color: var(--ink-dark); line-height: 24px; }
  .signatory__title { line-height: 22px; }
  .footer {
    position: absolute; left: 0; bottom: 0; width: 100%; height: 65px;
    background: var(--footer-navy);
    border-top: 8px solid var(--green-bar);
    display: flex; align-items: center; justify-content: center; gap: 20px;
    font-family: "Arimo", Arial, sans-serif; font-size: 17px; color: #fff;
  }
  .contact { display: flex; align-items: center; gap: 5px; }
  .contact svg { width: 26px; height: 26px; }
</style>
</head>
<body>
  <main class="letterhead">
    <div class="top-bar"></div>
    <div class="portrait" role="img" aria-label="Portrait photo of Clr Dariel Kostovenko in a dark suit on a light grey background"></div>
    <header class="identity">
      <h1 class="identity__name">Clr Dariel Kostovenko OAM</h1>
      <p class="identity__role">Candidate for Area Councillor<br>City of Darrow Bay</p>
    </header>

    <p class="meta">Issuing Date: May 5, 2018</p>
    <p class="recipient">Name Of Employee Mr. XYZABC<br>Address of Employee<br>Address Line 2 etc..</p>
    <p class="salutation">Dear Mr.XYZABC</p>

    <section class="letter-body">
      <p>Lorem Ipsum has been the industry's standard dummy text ever since the 1500s, when an unknown printer took a galley of type and scrambled it to make a type specimen book. It has survived not only five centuries, but also the leap into electronic typesetting, remaining essentially unchanged. It was popularised in the 1960s with the release of Transfix sheets containing Lorem Ipsum passages, and more recently with desktop publishing software like Quillon PageForge including versions of Lorem Ipsum.</p>
      <p>Lorem Ipsum is simply dummy text of the printing and typesetting industry. Lorem Ipsum has been the industry's standard dummy text ever since the 1500s, when an unknown printer took a galley of type and scrambled it to make a type specimen book.</p>
      <p>It has survived not only five centuries, but also the leap into electronic typesetting, remaining essentially unchanged. It was popularised in the 1960s with the release of Transfix sheets containing Lorem IpsumIpsum passages.</p>
    </section>

    <p class="sign-off">Yours Sincerely</p>
    <div class="signatory">
      <p class="signatory__name">Jonah Whitfield</p>
      <p class="signatory__title">Managing Director</p>
    </div>

    <footer class="footer">
      <span class="contact">
        <svg viewBox="0 0 26 26" aria-hidden="true"><circle cx="13" cy="13" r="11.5" fill="none" stroke="#fff" stroke-width="1.6"/><path d="M9.5 7.5c.8-.6 1.6-.4 2 .4l.9 1.8c.3.6.1 1.2-.4 1.6l-.7.5c.6 1.4 1.6 2.5 3 3.2l.5-.7c.4-.5 1-.7 1.6-.4l1.8.9c.8.4 1 1.2.4 2-1 1.3-2.4 1.7-3.9.9-2.9-1.5-5.1-3.800-6.3-6.6-.6-1.5-.1-2.8 1.1-3.6z" fill="#fff"/></svg>
        044-987 654 321
      </span>
      <span class="contact">
        <svg viewBox="0 0 26 26" aria-hidden="true"><circle cx="13" cy="13" r="11.5" fill="none" stroke="#fff" stroke-width="1.6"/><rect x="7" y="9" width="12" height="8.5" rx="1" fill="#fff"/><path d="M7.5 9.5l5.5 4.5 5.5-4.5" fill="none" stroke="#2a5f93" stroke-width="1.2"/></svg>
        info@darielko.com
      </span>
      <span class="contact">
        <svg viewBox="0 0 26 26" aria-hidden="true"><circle cx="13" cy="13" r="11.5" fill="none" stroke="#fff" stroke-width="1.6"/><g fill="none" stroke="#fff" stroke-width="1.2"><circle cx="13" cy="13" r="6.5"/><ellipse cx="13" cy="13" rx="3" ry="6.5"/><path d="M6.5 13h13M7.5 9.8h11M7.5 16.2h11"/></g></svg>
        www.darielko.com
      </span>
    </footer>
  </main>
</body>
</html>
```